News Framing & Public Opinion

We want a 4-color report that highlights the findings of a 2-part news and public opinion study. Such a report can be boring, so we would like it somewhat appealing to a variety of audiences. Audience members will be:
• American Indian tribal officials
• Fish and wildlife biologists
• US government officials

Goal is to have the report mailed in an envelope that can be sent USA Swiftline postage, but larger than the regulation #10 envelope. In the USA a larger first class envelope cannot be larger than:
6-1/8 inches high x 11-1/2 inches long x 1/4 inch thick

(For more information see
http://ref.parcelpostref.example/bulkmail202/sizerules/cards.htm)

MY PREFRENCE is the 6x9 envelope, which still qualifies for first class. A folded brochure is just fine.

The artwork is open (but MUST be copyright free) and should appeal to an educated, mature audience. This is a scientific report, and while it should be tasteful, it’s fine to have some impact and visual appeal.

I RECEIVED THE following tip from a designer for copyright free images. Here is the message:

Bureau of Waterworks digital visual library:
http://media.bowworks.example/sites/PIC/default.aspx

pics.lookfind.example

append "site:.gov" to the end of the query to only return images gathered from federal and state websites.

Artwork should not offend American Indian professionals, who are subject to stereotyping in media communication. A good example of tasteful communication can be seen at the website of the Cedar Valley Allied Rivers Council:
http://www.cvarc.example/
Updates

Check the cvarc website for possible art opportunities http://www.cvarc.example/
They also have a chatterbook page
Some ideas include:
1. Salmon
2.. Hollister dam
3. native fishers
4. fish spawning

Target Market(s)

scientists, professionals, native american governments, fishermen

Industry/Entity Type

Communication

Requirements
Must have
• tasteful
Nice to have
• artwork and visuals
Should not have
• stereotypes

```html
<!DOCTYPE html>
<html lang="en">
<head>
<meta charset="utf-8">
<title>News Framing &amp; Public Opinion – Study Findings</title>
<link href="https://fonts.googleapis.com/css2?family=Arimo:wght@400;700&family=Tinos:wght@400;700&display=swap" rel="stylesheet">
<style>
:root{
  --orange:#e8742a;
  --plum:#6e2a3a;
  --ink:#222;
  --peach:#fbeee4;
  --paper:#ffffff;
  --fish-red:#b8443a;
  --water:#3e6b6a;
}
*{box-sizing:border-box;margin:0;padding:0}
html,body{width:1200px;height:650px;overflow:hidden;background:var(--paper)}
body{font-family:"Tinos",serif;color:var(--ink)}
.spread{display:flex;width:1200px;height:650px}
.panel{width:400px;height:650px;position:relative;overflow:hidden}
.panel--conclusions{background:var(--peach);padding:14px 18px}
.questions{background:var(--orange);color:#fff;width:382px;height:206px;padding:16px 16px 0 22px}
.questions h2{font-family:"Arimo",sans-serif;font-weight:700;font-size:13px;letter-spacing:.2px;margin-bottom:6px}
.questions .lead{font-family:"Arimo",sans-serif;font-weight:700;font-size:9px;margin-bottom:6px}
.questions ul{list-style:none;font-size:8.4px;line-height:10.4px}
.questions li::before{content:"•";margin-right:6px}
.questions li{padding-left:8px}
.cols{display:flex;gap:12px;padding:12px 14px 0 22px}
.col{flex:1;font-size:8px;line-height:9.7px;overflow:hidden}
.col p{margin-bottom:6px}
h3{font-family:"Arimo",sans-serif;font-weight:700;font-size:10.5px;color:var(--plum);letter-spacing:.2px;margin:2px 0 5px;line-height:11px;text-transform:uppercase}
h4{font-family:"Arimo",sans-serif;font-weight:700;font-size:8.5px;color:var(--plum);margin-bottom:4px}
.pull{border-top:2.5px solid var(--orange);border-bottom:2.5px solid var(--orange);color:var(--orange);font-family:"Arimo",sans-serif;font-size:9.4px;line-height:11px;padding:8px 0 10px;margin:8px 0 10px}
.panel--middle .cols{padding:14px 14px 0 18px}
.panel--middle .pull{margin:6px 14px 0 18px}
.salmon-photo{display:block;margin:8px 14px 0 18px;width:368px;height:118px}
.conclusions-intro{font-size:10.6px;line-height:11.8px;margin-bottom:14px}
.panel--conclusions h3{font-size:11px;margin:4px 0 6px}
.panel--conclusions .cols{padding:0;gap:14px}
</style>
</head>
<body>
<main class="spread">

<section class="panel panel--left">
  <div class="questions">
    <h2>RESEARCH QUESTIONS</h2>
    <p class="lead">The study focused on the following research questions:</p>
    <ul>
      <li>Which frames dominated news coverage?</li>
      <li>Which news frames were reflected in residents' attitudes?</li>
      <li>Which stakeholders were most prominent in news coverage?</li>
      <li>Which stakeholders did residents say had the greatest stake in the issue?</li>
      <li>What types of environmental attitudes are held by local residents?</li>
      <li>Do residents favor lethal or non-lethal removal of sea lion?</li>
      <li>How do residents characterize Native American involvement in the issue?</li>
    </ul>
  </div>
  <div class="cols">
    <div class="col">
      <h3>News Coverage Summary</h3>
      <h4>Part 1</h4>
      <p>We examined coverage in Alaska, California, Idaho, Montana, Oregon and Washington from January 1, 2003, to June 21, 2010, for news related to sea lions and the Hollister Dam. The search yielded 161 news stories (and 223 editorials, letters to the editor, and opinions).</p>
      <p>Looking at news stories, we found the most prevalent themes (we call them “frames”) centered on blame, laws, successful solutions and failed solutions.</p>
      <p>Looking at the four most prominent frames, blame occurred most frequently (31% of all frames), followed by law frames (29%) and successful solutions (24%). Failed solutions accounted for 11% of frames.</p>
      <div class="pull">“Residents listed six factors affecting salmon decline: sea lions, politicians, Hollister Dam, commercial fishing, the federal government and environmental laws.”</div>
      <p>Blame most commonly focused on the sea lions: 47% of the “blame” stories said sea lions caused the salmon decline with another 14% crediting Hollister Dam for the problem. About 9% of blame frames focused on fishing and 5% mentioned environmental reasons as the cause.</p>
      <p>Law frames tended to mention protection of species, including both salmon and sea lions. The frame was also used to discuss the Kindred Animal League's legal actions to halt killing of sea lions.</p>
    </div>
    <div class="col">
      <p>Successful solutions and failed solutions typically featured the same issue: the removal of sea lions. In “successful” cases the stories reported that trapping sea lions prevents them from eating salmon. In contrast, some stories noted that trapping or hazing sea lions could be ineffective in removing them, and were characterized as “failed” solutions.</p>
      <h3>Sources</h3>
      <p>We also examined the types of sources quoted in news stories. Most sources (75%) in the timeframe were officials who represented the federal government and the states of Oregon and Washington.</p>
      <p>Advocacy groups such as the US Kindred Animal League, the Pinniped Guard Brigade and Open Waters Alliance were included as sources about 18% of the time, while tribal sources appeared in about 8% of stories.</p>
      <h4>Part 2</h4>
      <p>The second part of the study featured an attitude survey of residents of the Columbia River in December 2010. A random sample of 389 residents (55% women, 45% men) was selected. Average age was 58. Most (90%) considered their ethnicity as white, with the remaining stating their ethnicity as Native American, African, Asian, Latino or other. About 17% graduated from high school, and 80% had some college experience (40% graduated from college). About 11% earned $20,000 or less a year and 25% had an income between $20,000 and $50,000. About 54% had an income of $50,000 or higher.</p>
    </div>
  </div>
</section>

<section class="panel panel--middle">
  <div class="cols">
    <div class="col">
      <h3>Stakeholders</h3>
      <p>The news study showed that government sources (federal and state) were the most likely to be quoted (followed, with much less frequency, by advocacy sources and tribal sources). Residents, however, most frequently mentioned Native American tribes and commercial fishermen as key sources engaged in the issue: not government sources as noted in news stories. However, spokespeople from the state of Oregon and the State of Washington were mentioned with the next greatest frequency by local residents.</p>
      <p>Residents responded that sports fishermen, scientists and the Federal Government had a stake in the issue, although only moderately. The last three stakeholders – the Kindred Animal League, politicians and news reporters – were thought to have less interest in the issue.</p>
      <h3>Who's to Blame?</h3>
      <p>We asked residents their opinions about who is to blame for the decrease in salmon populations.</p>
      <p>Residents listed six factors affecting salmon decline: sea lions, politicians, Hollister Dam, commercial fishing, the federal government and environmental laws. Note that the responses aligned with some aspects of news coverage, which blamed sea lions, dams, fishing and environmental factors. Residents also blamed salmon loss partly on local government, farming, Native American fishermen and Native American governments. To a lesser extent, global warming, the news media, the economy, and birds were blamed for the salmon decrease.</p>
    </div>
    <div class="col">
      <h3>Environmental Attitudes</h3>
      <p>The study asked residents nine questions that measured environmental attitudes, ranging from views that human relationships with nature should be “balanced” to the idea that humans should “control nature.” Attitudes tended to align with balancing nature or controlling nature.</p>
      <h3>Are Attitudes Associated with Judgments?</h3>
      <p>We found attitudes about managing sea lions differed dramatically among residents. Those who favored balancing nature were more likely to blame global warming, the economy and Hollister Dam for salmon depletion. They favored relocating sea lions and were opposed to lethal removal.</p>
      <p>In contrast, residents who leaned toward controlling nature blamed the sea lions and were significantly less likely to blame Hollister Dam, farming or global warming. They favored lethal removal of sea lions.</p>
      <h3>Where Do Residents Get Their News?</h3>
      <p>Local TV news was used significantly more than any other information source. Other frequently used outlets included national TV news, the internet and local newspapers. Residents occasionally turned to chatterbook and radio talk shows, seldom read national newspapers and seldom talked with friends about the issue.</p>
    </div>
  </div>
  <div class="pull">“Solution frames highlighted the duel between agencies that claimed measures had been effective in managing the sea lions and special interest groups that claimed the measures had failed.”</div>
  <svg class="salmon-photo" role="img" aria-label="Photograph of red spawning salmon crowded in a shallow river" viewBox="0 0 368 118" preserveAspectRatio="none">
    <defs>
      <linearGradient id="riverTone" x1="0" y1="0" x2="1" y2="1">
        <stop offset="0" stop-color="#4f7470"/>
        <stop offset=".45" stop-color="#9b4a3f"/>
        <stop offset=".75" stop-color="#b8443a"/>
        <stop offset="1" stop-color="#3e5e5a"/>
      </linearGradient>
    </defs>
    <rect width="368" height="118" fill="url(#riverTone)"/>
  </svg>
</section>

<section class="panel panel--conclusions">
  <h3>Conclusions</h3>
  <p class="conclusions-intro">In summary, we found that news reporters from mainstream press favored official sources when covering the salmon and sea lion issue at the Columbia River. Other organizations – such as the Kindred Animal League – were quoted less often, with Native American sources quoted infrequently. Because the river, fish and wildlife are managed by federal and state agencies in concert with the tribes, it is reasonable that government sources would be quoted often in the press. However, the preponderance of official sources makes for less balanced coverage overall. We noted American Indian spokespeople are referenced infrequently, despite their stake in the Columbia River fisheries.</p>
  <div class="cols">
    <div class="col">
      <p>The conflictual nature of the issue resulted in news story frames that highlighted blame, laws and solutions (both successful and failed solutions). We found that the locus of blame centered on sea lions eating salmon at the Columbia River, while law frames focused on protection of species and the lawsuits over sea lion removal. Solution frames highlighted the duel between agencies that claimed measures had been effective in managing the sea lions and special interest groups that claimed the measures had failed.</p>
      <p>In some cases, the news coverage aligned with public opinion about the issue, while in other cases, opinion diverged from coverage. For example, both news and public opinion blamed sea lions as the cause of the conflict. Legal issues – noted in news coverage – were also mentioned by local residents as salient. Residents' opinions went beyond the news coverage. They blamed politicians, Hollister Dam, commercial fishing, the federal and local government, farming, Native American fishermen and Native American governments for the salmon decline.</p>
      <p>Stakeholder groups most often mentioned in news coverage represented government agencies. Local residents, however, saw the most prominent stakeholders as Native American tribes and commercial fishermen, followed by Oregon and Washington officials. The US Kindred Animal League – which brought legal action against the sea lion removal – was low on the list of stakeholders engaged in the issue, according to the public opinion survey.</p>
    </div>
    <div class="col">
      <p>Views about sea lion management align along environmental attitudes. Residents who endorsed environmental protection blamed global warming, the economy and Hollister Dam and were opposed to killing sea lions. In contrast, residents who believed in controlling nature blamed the sea lions and favored lethal removal.</p>
      <div class="pull">“Press coverage does not appear to be a reliable indicator of public opinion of residents who live near the Columbia River.”</div>
      <p>The studies demonstrate that mainstream news coverage surrounding sea lions at the Columbia River was treated in conflictual ways and that residents who live in proximity of the river – in Oregon and Washington – mirror the coverage in some ways and diverge in others. Residents were likely to agree with the news that sea lions were responsible for salmon depletion and, to a lesser extent, the dam, but residents also blamed politicians, commercial fishing, the federal government and environmental laws, which received scant coverage.</p>
      <p>In other words, press coverage does not appear to be a reliable indicator of public opinion of residents who live near the Columbia River. Attitudes about nature and the environment appear to be a promising indicator of attribution of blame concerning salmon depletion and beliefs about sea lion management.</p>
    </div>
  </div>
</section>

</main>
</body>
</html>
```